Design a Google site for a travel agency

I own a travel agency and I would like to have a Google site built for my company called Wavetrailjourneys.example by Brisk Harbor Getaways. Our specialty Cruising and adventure. We create a lot of custom tour of Europe and Peru. Our Adventure tours targets mainly women from 25 to 65. I would like to site especially the cruise to appeal to family but also upscale more expensive upscale clientele.
Updates

I would like to shift away from create a new site with multiple pages to one simple Google Site page with a Contact us page and testimonials. The sites theme is Cruise & Adventure Travel. We specialize in selling cruises and building custom travel tours around the world.

Target Market(s)

Cruisers and adventure travelers for women from 25 to 70

Industry/Entity Type

travel industry with a focus on cruising and adventure travel

Coding

Coded - Design and coding required

Number of Pages Required

5+ page

Font styles to use
Serif
Sans Serif

Requirements
Must have
• Home page, Cruise, Adventure Tours, Testimonials, About Us
Nice to have
• Auto place https://www.briskharborgetaways.example/offers into the site.
Should not have
• beach resorts

```html
<!DOCTYPE html>
<html lang="en">
<head>
<meta charset="utf-8">
<title>Brisk Harbor Getaways – Cruise &amp; Adventure Tours</title>
<link rel="stylesheet" href="https://fonts.googleapis.com/css2?family=Playfair+Display:wght@400&family=Poppins:wght@400;600&family=Open+Sans:wght@400;600&display=swap">
<style>
  :root {
    --ink: #1f1f1f;
    --muted: #5a5a5a;
    --header-bg: #000000;
    --nav-text: #ffffff;
    --orange: #f39a1e;
    --sky: #2f9fd8;
    --pink: #ea6a9d;
    --band: #fbb900;
    --page: #ffffff;
    --map-bg: #eef0f2;
  }
  * { box-sizing: border-box; margin: 0; padding: 0; }
  html, body { width: 1200px; height: 2206px; overflow: hidden; background: var(--page); }
  .site { position: relative; width: 1200px; height: 2206px; color: var(--ink); font-family: "Open Sans", sans-serif; }

  .site-header { position: absolute; top: 0; left: 0; width: 1200px; height: 44px; background: var(--header-bg); display: flex; align-items: center; padding: 0 20px 0 24px; }
  .brand { display: flex; align-items: center; gap: 8px; font-family: "Poppins", sans-serif; font-weight: 400; font-size: 15px; color: var(--orange); }
  .brand-dot { width: 14px; height: 14px; border-radius: 50%; background: var(--orange); }
  .main-nav { margin-left: auto; display: flex; align-items: center; gap: 14px; font-size: 14px; color: var(--nav-text); }
  .main-nav .current { font-weight: 600; }
  .main-nav .sep { opacity: .7; }
  .search-icon { margin-left: 14px; }

  .hero { position: absolute; top: 44px; left: 0; width: 1200px; height: 329px; background: linear-gradient(100deg, #18231c 0%, #2c3a30 30%, #4c5a4a 55%, #7a6a55 80%, #9a7d60 100%); }
  .hero-title { position: absolute; left: 159px; top: 78px; font-family: "Playfair Display", serif; font-weight: 400; font-size: 52px; line-height: 59px; }
  .hero-title .warm { color: var(--orange); }
  .hero-title .cool { color: var(--sky); }

  .welcome { position: absolute; top: 404px; left: 0; width: 1200px; text-align: center; }
  .welcome h1 { font-family: "Playfair Display", serif; font-weight: 400; font-size: 40px; color: var(--ink); }
  .welcome h1 span { color: var(--orange); }
  .welcome p { width: 880px; margin: 18px auto 0; font-family: "Poppins", sans-serif; font-size: 9.5px; line-height: 19px; color: var(--muted); }

  .services { position: absolute; top: 550px; left: 154px; display: flex; gap: 23px; }
  .service { width: 282px; text-align: center; }
  .service-photo { width: 282px; height: 282px; }
  .service h2 { margin-top: 14px; font-family: "Poppins", sans-serif; font-weight: 600; font-size: 19px; color: var(--pink); }
  .service p { margin-top: 22px; padding: 0 14px; font-family: "Poppins", sans-serif; font-size: 12.5px; line-height: 19px; color: #444; }

  .testimonials { position: absolute; top: 999px; left: 0; width: 1200px; height: 274px; background: var(--band); text-align: center; }
  .testimonials h2 { margin-top: 68px; font-family: "Playfair Display", serif; font-weight: 400; font-size: 38px; text-decoration: underline; text-underline-offset: 5px; text-decoration-thickness: 2px; color: #111; }
  .testimonials p { width: 730px; margin: 16px auto 0; font-size: 13px; line-height: 19px; color: #222; }

  .location-map { position: absolute; top: 1292px; left: 154px; width: 891px; height: 350px; background: linear-gradient(135deg, #f2f3f4, #e6e8ea); }

  .contact { position: absolute; top: 1750px; left: 161px; font-family: "Poppins", sans-serif; }
  .contact-item { margin-bottom: 37px; }
  .contact-item h3 { font-weight: 600; font-size: 15px; color: var(--orange); }
  .contact-item p { margin-top: 10px; font-size: 12.5px; color: #222; }
  .coast-photo { position: absolute; top: 1741px; left: 536px; width: 511px; height: 292px; background: linear-gradient(160deg, #3b7fb6 0%, #7cc6e0 30%, #4fd0cf 55%, #2f6a3a 75%, #9fe3df 100%); }

  .site-footer { position: absolute; top: 2104px; left: 0; width: 1200px; display: flex; justify-content: center; }
  .site-footer .brand { font-size: 26px; }
  .site-footer .brand-dot { width: 20px; height: 20px; }
</style>
</head>
<body>
<div class="site">
  <header class="site-header">
    <div class="brand"><span class="brand-dot"></span>Brisk Harbor Getaways</div>
    <nav class="main-nav">
      <span class="current">Home</span><span class="sep">·</span>
      <span>About Us</span><span class="sep">·</span>
      <span>Cruise</span><span class="sep">·</span>
      <span>Adventure Tours</span><span class="sep">·</span>
      <span>CALL NOW: 555-014-2290</span>
      <svg class="search-icon" width="15" height="15" viewBox="0 0 16 16" aria-hidden="true"><circle cx="6.5" cy="6.5" r="5" fill="none" stroke="#fff" stroke-width="1.8"/><line x1="10.2" y1="10.2" x2="15" y2="15" stroke="#fff" stroke-width="1.8"/></svg>
    </nav>
  </header>

  <section class="hero" role="img" aria-label="Lakeside alpine village with a church spire and a boat on calm water">
    <h1 class="hero-title"><span class="warm">Cruise &amp;</span><br><span class="cool">Adventure</span><br><span class="warm">Tours</span></h1>
  </section>

  <section class="welcome">
    <h1>Welcome to <span>Brisk Harbor Getaways</span></h1>
    <p>Lorem ipsum dolor sit amet, consectetur adipiscing elit. Sed et malesuada sem, non rhoncus leo. Praesent ut nulla malesuada, commodo dolor non, finibus enim. Proin egestas urna vel arcu mattis, in sagittis libero aliquet. Suspendisse potenti. Praesent scelerisque bibendum leo sit amet dignissim. Cras iaculis pulvinar hendrerit.</p>
  </section>

  <section class="services">
    <article class="service">
      <div class="service-photo" role="img" aria-label="Glacier lagoon with floating icebergs" style="background:linear-gradient(180deg,#c9d3de 0%,#e6edf2 40%,#8fb6c4 70%,#4f8a98 100%)"></div>
      <h2>Advanture</h2>
      <p>Lorem ipsum dolor sit amet, consectetur adipiscing elit. Sed et malesuada sem, non rhoncus leo. Praesent ut nulla malesuada, commodo dolor non, finibus enim.</p>
    </article>
    <article class="service">
      <div class="service-photo" role="img" aria-label="Wooden pier on a mountain lake under a moonlit sky" style="background:linear-gradient(180deg,#1b4f8e 0%,#2f6fb0 35%,#16324a 60%,#2a5a7a 80%,#3b3a2c 100%)"></div>
      <h2>Holidays</h2>
      <p>Lorem ipsum dolor sit amet, consectetur adipiscing elit. Sed et malesuada sem, non rhoncus leo. Praesent ut nulla malesuada, commodo dolor non, finibus enim.</p>
    </article>
    <article class="service">
      <div class="service-photo" role="img" aria-label="Tropical island with palm trees and turquoise water" style="background:linear-gradient(180deg,#1c5fb8 0%,#6aa6e0 30%,#4f8a2e 55%,#e8e2d0 70%,#3fc6d6 100%)"></div>
      <h2>Tourist</h2>
      <p>Lorem ipsum dolor sit amet, consectetur adipiscing elit. Sed et malesuada sem, non rhoncus leo. Praesent ut nulla malesuada, commodo dolor non, finibus enim.</p>
    </article>
  </section>

  <section class="testimonials">
    <h2>What our customer Says</h2>
    <p>Lorem ipsum dolor sit amet, consectetur adipiscing elit. Sed et malesuada sem, non rhoncus leo. Paesent ut nulla malesuada, commodo dolor non, finibus enim. Lorem ipsum dolor sit amet, consectetur adipiscing elit. Sed et malesuada sem, non rhoncus leo. Paesent ut nulla malesuada, commodo dolor non, finibus enim.</p>
  </section>

  <div class="location-map" role="img" aria-label="Street map showing the agency office location"></div>

  <section class="contact">
    <div class="contact-item"><h3>Call:</h3><p>555-014-2290</p></div>
    <div class="contact-item"><h3>Location:</h3><p>18 Harbour Lane, Riverton, NB, E0A 1B2, Canada</p></div>
    <div class="contact-item"><h3>Email:</h3><p>hello@briskharborgetaways.example</p></div>
  </section>
  <div class="coast-photo" role="img" aria-label="Aerial view of a sandy coastline and turquoise lagoon"></div>

  <footer class="site-footer">
    <div class="brand"><span class="brand-dot"></span>Brisk Harbor Getaways</div>
  </footer>
</div>
</body>
</html>
```